Computer consultant website

Plivet Software is a newly started computer consulting company. It's a small one-man company that provides mostly Android applications but also websites in collaboration with designers. I'm running this company on the side of full time university studies.

I'm in need of a website which will function as:
Primarily - I'll direct potential clients to the page so they can read about the company, what i offer and past work.
Secondarily - Making my company visible through the web and maybe getting new clients.

The final design should look modern, clean and professional.

Pages that will be in the final website are (Note that it's not the exact titles as the page will not be in english):
* About
* Services (what Plivet offers)
* Portfolio/work
* Short news (like Framolines "News and press")
* Contact.

Inspiration
http://www.framoline.example/design/87836
http://www.quarnbelt.example/
http://www.framoline.example/design/845881
http://www.framoline.example/design/1369424 - Lighter design, however a bit cluttered.

No programming code is needed delivered at all. Focus on designing rather then coding.

If you have any questions, do not hesitate to send me a message.

Target Market(s)

Non-technical entrepreneurs and small companies.

Industry/Entity Type

University

Requirements
Must have
• Must have my company logo (see attachment).

Must in any way use both colors from my logo.

A way to logically rearrange content to fit smaller screens. I will implement this design so that it can be pleasantly viewed on mobile devices. You don't necessarily need to provide exactly how the design would look on mobile devices.

I need the following types of page designs:
* Landing page
* Content page
* Portfolio/work (with accompanying inside/clicked) page

Landing/start page must in any way include at least the information:
* Shorter version of "About Plivet"
* At least 1 most recent portfolio/work entry
* At least 1 most recent news entry
* Services that Plivet offers.
Nice to have
• -
Should not have
• Testimonials or newsletter.

```html
<!DOCTYPE html>
<html lang="en">
<head>
<meta charset="utf-8">
<title>Plivet Software</title>
<link rel="stylesheet" href="https://fonts.googleapis.com/css2?family=Open+Sans:wght@300;400;600;700&display=swap">
<style>
:root{
  --ink:#363334;
  --nav:#363334;
  --blue:#2a7cf6;
  --blue-light:#7eb0fb;
  --navy:#12306e;
  --text:#4a4a4a;
  --muted:#6b6b6b;
  --panel:#f3f3f3;
  --footer:#2e2d2d;
  --footer-text:#d8d8d8;
}
*{margin:0;padding:0;box-sizing:border-box}
html,body{width:1120px;height:1200px;overflow:hidden}
body{position:relative;background:#fff;font-family:"Open Sans",sans-serif;color:var(--text)}
.abs{position:absolute}
.line{white-space:nowrap}

.top-nav{left:0;top:0;width:1120px;height:48px;background:var(--nav)}
.top-nav ul{list-style:none;position:absolute;left:160px;top:0;display:flex;height:48px}
.top-nav li{color:#fff;font-size:14.5px;line-height:48px;padding:0 15px}
.top-nav li.active{background:var(--blue);padding:0 17px}

.brand{left:160px;top:74px;display:flex;align-items:center;gap:12px}
.brand-dot{width:46px;height:46px;border-radius:50%;background:var(--blue)}
.brand-name{font-size:42px;font-weight:600;color:var(--ink);letter-spacing:-1px}

.consult{left:782px;top:80px;display:flex;gap:6px}
.consult-label{color:var(--blue);font-size:19.5px;line-height:20px}
.consult-phone{color:var(--ink);font-size:23px;font-weight:700;line-height:26px}

.hero{left:160px;top:157px;width:794px;height:310px;border:1px solid #dcdcdc;
  background:linear-gradient(90deg,#e6eef3 0%,#f1f6f9 40%,#d7e8f2 100%)}
.hero-photo{left:0;top:0;width:380px;height:308px;background:linear-gradient(180deg,#cfd4d8,#e9ecef)}
.hero-title{left:401px;top:108px;font-size:40px;font-weight:300;line-height:39px;color:var(--ink)}
.hero-title em{font-style:normal;color:var(--blue)}

.services{left:147px;top:467px;width:807px;height:100px;background:var(--blue);display:flex}
.services-tab{width:128px;height:100px;position:relative}
.services-tab svg{position:absolute;left:0;top:0}
.services-tab h2{position:absolute;left:16px;top:26px;font-size:19px;font-weight:700;line-height:19px;color:var(--navy)}
.service{flex:1;border-left:1px solid #5b9af8;text-align:center;color:#fff;font-size:12px;font-weight:700;line-height:14.5px;padding-top:16px}
.service:first-of-type{border-left:none}
.service svg{display:block;margin:0 auto 6px}
.bar-shadow{left:170px;top:567px;width:760px;height:20px;background:radial-gradient(ellipse at top,rgba(0,0,0,.18),rgba(0,0,0,0) 70%)}

.why h1{left:167px;top:598px;font-size:24px;font-weight:400;line-height:32px;color:#222}
.why h3{left:170px;font-size:12px;font-weight:700;line-height:16px;color:var(--blue)}
.why p{left:170px;font-size:11.4px;line-height:17.6px}
.more-link{font-size:11.4px;line-height:16px;color:var(--blue);text-decoration:underline;white-space:nowrap}
.more-link::after{content:"\203A";text-decoration:none;display:inline-block;margin-left:8px;color:#333}

.news{left:168px;top:821px;width:510px;height:212px;background:var(--panel);border:1px solid #dedede;box-shadow:0 1px 3px rgba(0,0,0,.1)}
.news h2{left:17px;top:4px;font-size:19.5px;font-weight:400;line-height:30px;color:#222}
.news hr{position:absolute;left:18px;top:38px;width:472px;border:0;border-top:1px solid #e0e0e0}
.news-client{left:18px;top:62px;display:flex;align-items:center;gap:6px}
.news-client span:first-child{width:12px;height:12px;background:var(--navy)}
.news-client span:last-child{font-size:18px;font-weight:700;line-height:24px;color:var(--navy)}
.news-title{left:143px;top:52px;font-size:19px;font-weight:400;line-height:26px;color:var(--blue);letter-spacing:-.2px}
.news-meta{left:145px;top:77px;font-size:9.5px;line-height:12px;color:#666}
.news-text{left:143px;top:98px;font-size:11.4px;line-height:17.6px}
.news-more{left:143px;top:173px}

.recent{left:720px;top:600px;font-size:19.5px;font-weight:400;line-height:30px;color:#222}
.work-shot{left:720px;top:638px;width:218px;height:186px;background:linear-gradient(180deg,#3b3b3b 0%,#2a2a2a 68%,#d9d9d9 72%,#c2c2c2 100%);border-radius:4px}
.work-site{left:725px;top:834px;font-size:12px;font-weight:700;line-height:16px;color:var(--blue)}
.work-label{left:725px;top:856px;font-size:11.4px;line-height:14px;color:#333;text-transform:uppercase}
.work-text{left:725px;top:872px;font-size:11.4px;line-height:17.6px;color:var(--muted)}
.btn-works{left:726px;top:992px;width:210px;height:42px;border:1px solid #c9c9c9;background:linear-gradient(#e3e3e3,#bdbdbd);color:#555;font-size:14.5px;font-weight:700;text-align:center;line-height:40px}

.site-footer{left:0;top:1072px;width:1120px;height:128px;background:var(--footer)}
.footer-nav{left:175px;top:38px;display:flex;gap:23px;list-style:none;font-size:11.6px;color:#fff}
.footer-copy{left:175px;top:69px;font-size:11.6px;color:var(--footer-text)}
.touch{left:726px;top:24px;width:190px;text-align:center}
.touch-title{font-size:11.6px;color:#fff;display:flex;align-items:center;gap:6px}
.touch-title::before,.touch-title::after{content:"";flex:1;border-top:1px solid #555}
.social{display:flex;gap:5px;justify-content:center;margin-top:5px}
.social span{width:32px;height:32px;border-radius:50%;background:#9a9a9a}
.call{margin-top:10px;font-size:11.6px;color:var(--blue-light)}
</style>
</head>
<body>

<nav class="top-nav abs">
  <ul><li class="active">Home</li><li>About</li><li>Services</li><li>Works</li><li>News</li><li>Contact</li></ul>
</nav>

<div class="brand abs"><span class="brand-dot"></span><span class="brand-name">plivet</span></div>

<div class="consult abs">
  <svg width="18" height="40" viewBox="0 0 18 40"><rect x="1" y="1" width="16" height="38" rx="2" fill="none" stroke="#6b6b6b" stroke-width="2"/><rect x="4" y="4" width="10" height="12" fill="#6b6b6b"/><g fill="#6b6b6b"><rect x="4" y="20" width="3" height="3"/><rect x="10" y="20" width="3" height="3"/><rect x="4" y="26" width="3" height="3"/><rect x="10" y="26" width="3" height="3"/><rect x="4" y="32" width="3" height="3"/><rect x="10" y="32" width="3" height="3"/></g></svg>
  <div><div class="consult-label">Free Consultancy</div><div class="consult-phone">010 55 2 4170</div></div>
</div>

<section class="hero abs">
  <div class="hero-photo abs" role="img" aria-label="Photo of a consultant in shirt and tie talking on a mobile phone"></div>
  <h1 class="hero-title abs">WE ASSURE <em>YOU</em><br>QUALITY <em>WORK</em></h1>
</section>

<section class="services abs">
  <div class="services-tab">
    <svg width="130" height="100"><defs><linearGradient id="tabGrad" x1="0" y1="0" x2="1" y2="0"><stop offset="0" stop-color="#a9c8fb"/><stop offset="1" stop-color="#6fa4f8"/></linearGradient></defs><polygon points="0,0 106,0 128,50 106,100 0,100" fill="url(#tabGrad)"/></svg>
    <h2>Services<br>We Offer</h2>
  </div>
  <div class="service">
    <svg width="40" height="44" viewBox="0 0 40 44"><rect x="10" y="4" width="20" height="34" rx="3" fill="#fff"/><rect x="13" y="8" width="14" height="22" fill="#2a7cf6"/><circle cx="20" cy="34" r="1.8" fill="#2a7cf6"/></svg>
    Android App<br>Development
  </div>
  <div class="service">
    <svg width="40" height="44" viewBox="0 0 40 44"><rect x="7" y="4" width="26" height="24" rx="2" fill="#fff"/><rect x="11" y="8" width="18" height="14" fill="#2a7cf6"/><rect x="4" y="30" width="32" height="8" rx="2" fill="#fff"/></svg>
    Web App<br>Development
  </div>
  <div class="service">
    <svg width="40" height="44" viewBox="0 0 40 44"><circle cx="17" cy="17" r="11" fill="none" stroke="#fff" stroke-width="5"/><line x1="25" y1="25" x2="35" y2="37" stroke="#fff" stroke-width="6" stroke-linecap="round"/></svg>
    Search Engine<br>Optimization
  </div>
  <div class="service">
    <svg width="40" height="44" viewBox="0 0 40 44"><path d="M36 4 L16 28 L12 24 Z" fill="#fff"/><path d="M11 26 L15 30 C12 37 7 39 3 38 C6 35 5 29 11 26 Z" fill="#fff"/></svg>
    User Experience<br>Design
  </div>
</section>
<div class="bar-shadow abs"></div>

<section class="why">
  <h1 class="abs">Why should you choose us</h1>
  <h3 class="abs line" style="top:632px">consectetur adipiscing elit</h3>
  <p class="abs line" style="top:649px">Aenean metus mauris, auctor eget interdum id, imperdiet a lorem. Proin vitae elit ante, sit amet<br>sollicitudin eros. Lorem ipsum dolor sit amet, consectetur adipiscing elit. Nam neque mauris,<br>eleifend eget vestibulum non</p>
  <h3 class="abs line" style="top:720px">Nunc viverra fringilla arcu aliquam rutrum</h3>
  <p class="abs line" style="top:737px">Cras fringilla elit nunc, eget vulputate odio. Fusce semper nibh eu tellus facilisis ut porttitor urna<br>auctor. Aenean luctus molestie ante non porta. Morbi sollicitudin pretium dolor. Cras gravida</p>
  <a class="more-link abs" style="left:171px;top:777px">Explore More About us</a>
</section>

<section class="news abs">
  <h2 class="abs">Current News</h2>
  <hr>
  <div class="news-client abs"><span></span><span>Sorvane</span></div>
  <h3 class="news-title abs line">Cum sociis natoque penatibus et magnis</h3>
  <div class="news-meta abs line">27th February 2012 | Sorvane</div>
  <p class="news-text abs line">Cras fringilla elit nunc, eget vulputate odio. Fusce semper nibh eu<br>tellus facilisis ut porttitor urna auctor. Aenean luctus molestie ante<br>non porta. Morbi sollicitudin pretium dolor. Cras gravida lobortis<br>eleifend. Etiam auctor</p>
  <a class="more-link news-more abs">Read More News</a>
</section>

<h2 class="recent abs">Most Recent Work</h2>
<div class="work-shot abs" role="img" aria-label="Screenshot of the Plivet website shown on a desktop monitor"></div>
<h3 class="work-site abs">plivet.example</h3>
<h4 class="work-label abs">Project Overview</h4>
<p class="work-text abs line">Tincidunt sit amet auctor a, lobortis non<br>eros. Proin a lorem a nibh volutpat<br>euismod. Pellentesque commodo mattis<br>augue vitae sagittis. In hac habitasse<br>platea dictumst. Cum sociis natoque<br>penatibus et magnis dis parturient</p>
<div class="btn-works abs">VIEW ALL OUR WORKS</div>

<footer class="site-footer abs">
  <ul class="footer-nav abs"><li>Home</li><li>About</li><li>Services</li><li>Works</li><li>News</li><li>Contact</li></ul>
  <div class="footer-copy abs">Copyright © 2013 Plivet. All rights reserved | Terms and Conditions | Privacy Policy</div>
  <div class="touch abs">
    <div class="touch-title">KEEP IN TOUCH</div>
    <div class="social"><span></span><span></span><span></span><span></span><span></span></div>
    <div class="call">Call us at&nbsp; 010 552 4170</div>
  </div>
</footer>

</body>
</html>
```